32 x 24 Swinging Real Estate Yard Sign

We are looking to design a new sign for our business to focus on the remodeling of homes to sell. We are looking to have a yard sign that gets peoples attention and is informational. The headline will be "The Secret to Top Dollar? Remodel First.". We remodel homes for sellers with no up front cost, as they simply pay at closing. This link has more info, https://brightkeelhomes.com/Remodel
The message we want to convey to those seeing the sign is we are a one stop shop, who can renovate your home and sell it for no stress. We are licensed real estate agents and licensed contractors.
Both of these license numbers and info need to be on the design:
CADRE #07264918
Contractors License #2851736
Email: info@brightkeelhomes.com
Phone: (408)555-0183
I'll attach a sample sign we have for our agents normally as well as all brand art work.
• Pantone Colors
o #172A41
Dark blue
o #4381B1
Medium blue
o #6FA6CC
Light blue
Target Market(s)
Residential Real Estate Sellers
Industry/Entity Type
Real Estate
Colors
Designer to choose colors to be used in the design.

```html
<!DOCTYPE html>
<html lang="en">
<head>
<meta charset="utf-8">
<title>Brightkeel Homes – Remodel First Yard Sign</title>
<link rel="stylesheet" href="https://fonts.googleapis.com/css2?family=Poppins:wght@400;500;700&family=Oswald:wght@700&display=swap">
<style>
  :root{
    --navy:#172A41;
    --mid-blue:#4381B1;
    --light-blue:#6FA6CC;
    --white:#ffffff;
    --shadow:#0b0f16;
    --page:#eef1f4;
  }
  html,body{margin:0;padding:0;width:1200px;height:1200px;overflow:hidden;background:var(--page);}
  .canvas{position:relative;width:1200px;height:1200px;}
  .yard-sign{
    position:absolute;left:50px;top:187px;
    width:1158px;height:868px;
    transform:scale(0.95);transform-origin:0 0;
    background:var(--navy);overflow:hidden;
    font-family:"Poppins",sans-serif;
  }
  .sign-shapes{position:absolute;inset:0;width:100%;height:100%;}
  .brand{
    position:absolute;left:60px;top:175px;width:390px;
    display:flex;flex-direction:column;align-items:center;gap:12px;
  }
  .brand-dot{width:58px;height:58px;border-radius:50%;background:var(--light-blue);}
  .brand-name{
    margin:0;color:var(--white);font-weight:500;font-size:46px;line-height:1.05;
    text-align:center;letter-spacing:1px;
  }
  .headline{
    position:absolute;left:508px;top:42px;margin:0;
    font-weight:700;font-size:76px;line-height:95px;letter-spacing:-0.5px;
    color:var(--white);text-transform:uppercase;white-space:nowrap;
  }
  .headline .accent{color:var(--light-blue);display:block;}
  .licenses{
    position:absolute;left:276px;top:418px;width:608px;height:94px;
    display:flex;flex-direction:column;align-items:center;justify-content:center;
    color:var(--navy);font-size:30px;font-weight:400;line-height:1.2;
  }
  .email{
    position:absolute;left:0;right:0;top:555px;text-align:center;
    color:var(--white);font-size:58px;font-weight:400;
  }
  .phone{
    position:absolute;left:0;right:0;top:642px;text-align:center;
    font-family:"Oswald",sans-serif;font-weight:700;font-size:178px;line-height:1;
    color:var(--white);letter-spacing:2px;
    transform:scaleX(0.9);
    text-shadow:-7px 7px 0 var(--shadow);
  }
</style>
</head>
<body>
<main class="canvas">
  <section class="yard-sign" aria-label="Brightkeel Homes remodel yard sign">
    <svg class="sign-shapes" viewBox="0 0 1158 868" preserveAspectRatio="none" aria-hidden="true">
      <path class="lower-band" fill="var(--mid-blue)"
        d="M0 200 C 15 390, 130 470, 280 472 L 1000 472 C 1095 472, 1150 540, 1158 640 L1158 868 L0 868 Z"/>
      <path class="band-edge" fill="none" stroke="var(--white)" stroke-width="10"
        d="M0 200 C 15 390, 130 470, 280 472 L 1000 472 C 1095 472, 1150 540, 1158 640"/>
      <rect class="license-pill" x="276" y="418" width="608" height="94" rx="47"
        fill="var(--light-blue)" stroke="var(--navy)" stroke-width="9"/>
    </svg>

    <div class="brand">
      <span class="brand-dot"></span>
      <p class="brand-name">BRIGHTKEEL<br>HOMES</p>
    </div>

    <h1 class="headline">The Secret to<br>Top Dollar?<span class="accent">Remodel First</span></h1>

    <div class="licenses">
      <span class="license-agent">CADRE #07264918</span>
      <span class="license-contractor">Contractors License #2851736</span>
    </div>
    <div class="email">info@brightkeelhomes.com</div>
    <div class="phone">408 555 0183</div>
  </section>
</main>
</body>
</html>
```